Business Card Design

I need a business card design for my new solo law practice. I practice consumer bankruptcy law.

I would like a simple, functional business card that looks professional but will also be understandable to regular people - not just other lawyers.
Updates

I added a couple of possible logos that can be incorporated

I'm sorry about the confusion, but the suite number for my new office is suite #214. Thanks for your patience

Target Market(s)

the real target market is potential clients

Industry/Entity Type

Business

Contact Information for Business Card

Law Offices of Theodore M. Vance
Theodore M. Vance
Attorney at Law
Bankruptcy Law
418 Marlowe Court #150
Harlow Springs, PA 16022
(555) 317-6482 (Phone)
(555) 317-6497 (Fax)
theov@cedarpointdebtrelief.example
cedarpointdebtrelief.example

Font styles to use
Serif

Requirements
Nice to have
• I've added some possible logos to possible incorporate

```html
<!DOCTYPE html>
<html lang="en">
<head>
<meta charset="utf-8">
<title>Theodore M. Vance — Business Card</title>
<link rel="stylesheet" href="https://fonts.googleapis.com/css2?family=Saira:wght@400;500&display=swap">
<style>
  :root {
    --backdrop: #b9bbbe;
    --card-green: #8cc63f;
    --card-cream: #eef3de;
    --navy: #2b4a7a;
    --ink: #33415c;
    --accent-red: #9e1b20;
    --white: #ffffff;
    --disc-green: #cfe6a8;
  }
  * { box-sizing: border-box; margin: 0; padding: 0; }
  html, body { width: 1200px; height: 900px; overflow: hidden; }
  body {
    background: var(--backdrop);
    font-family: "Saira", "Helvetica Neue", Arial, sans-serif;
    display: flex;
    align-items: center;
    justify-content: center;
    gap: 60px;
  }
  .card {
    position: relative;
    width: 520px;
    height: 298px;
    border-radius: 22px;
    overflow: hidden;
    box-shadow: 0 6px 18px rgba(0,0,0,0.22);
  }
  /* Front */
  .card-front {
    background: var(--card-green);
    display: flex;
    flex-direction: column;
    align-items: center;
    justify-content: center;
  }
  .firm-mark {
    width: 92px;
    height: 92px;
    border-radius: 50%;
    border: 8px solid var(--navy);
    background: var(--disc-green);
    margin-bottom: 22px;
  }
  .firm-name {
    color: var(--navy);
    font-size: 29px;
    font-weight: 400;
    letter-spacing: 0.2px;
    white-space: nowrap;
  }
  .firm-url {
    margin-top: 14px;
    color: var(--white);
    font-size: 11px;
    letter-spacing: 3.2px;
  }
  /* Back */
  .card-back { background: var(--card-cream); }
  .back-ring {
    position: absolute;
    right: -150px;
    top: -20px;
    width: 330px;
    height: 330px;
  }
  .contact {
    position: absolute;
    left: 34px;
    top: 88px;
    color: var(--ink);
  }
  .contact-name {
    color: var(--accent-red);
    font-size: 25px;
    font-weight: 400;
    margin-bottom: 18px;
  }
  .contact-role, .contact-address { font-size: 13px; line-height: 1.35; white-space: nowrap; }
  .contact-lines { margin-top: 16px; list-style: none; font-size: 13px; line-height: 1.4; }
  .contact-lines .label { color: var(--accent-red); }
  .contact-web { color: var(--accent-red); }
</style>
</head>
<body>
  <section class="card card-front">
    <div class="firm-mark" aria-hidden="true"></div>
    <h1 class="firm-name">Law Offices of Theodore M. Vance</h1>
    <p class="firm-url">www.cedarpointdebtrelief.example</p>
  </section>

  <section class="card card-back">
    <svg class="back-ring" viewBox="0 0 330 330" aria-hidden="true">
      <defs>
        <radialGradient id="disc-fill" cx="40%" cy="45%" r="60%">
          <stop offset="0%" stop-color="#ffffff"/>
          <stop offset="100%" stop-color="#9fcf62"/>
        </radialGradient>
      </defs>
      <circle cx="165" cy="165" r="150" fill="url(#disc-fill)" stroke="#2b4a7a" stroke-width="16"/>
    </svg>
    <div class="contact">
      <h2 class="contact-name">Theodore M. Vance</h2>
      <p class="contact-role">Attorney at Law Bankruptcy Law</p>
      <p class="contact-address">418 Marlowe Court #214 Harlow Springs, PA 16022</p>
      <ul class="contact-lines">
        <li><span class="label">P:</span> (555) 317-6482</li>
        <li><span class="label">F:</span> (555) 317-6497</li>
        <li><span class="label">E:</span> theov@cedarpointdebtrelief.example</li>
        <li class="contact-web">www.cedarpointdebtrelief.example</li>
      </ul>
    </div>
  </section>
</body>
</html>
```